International Accounting, Law and Real Estate firm needs a English-Spanish web design

We are a firm dedicated to accounting-taxes, Legal and Real Estate in the northern part of Mexico on the border with Arizona USA, so our clients are half Mexicans and Half Americans. We are located on the coast (Puerto Peñasco, also called Rocky Point). Our name is CORA ADVISORY, where REAL stands for:
R=real
E= estate
A= Accounting
L= Legal
our web page is www.coraadvisory.com.mx, we need something more attractive, profesional, fresh, inviting, and we need to have it in English and a Spanish and I need to be able to keep uploading new properties for sale.
Our number one activity now is Accounting and Taxes, we are growing on the legal side and there is a huge opportunity in the market to help Foreigners get their property titles, and our third activity is Real Estate. We have an excellent reputation of honesty and professional people. We would like to advertise as a ONE PLACE for Legal and Taxes matters. Or also something like Your Taxes and Trust specialists... or Total solutions with Integrity ....

Target Market(s)

local business and US visitors some of them do business in Mexico, others buy properties and need legal help to be able to get their title (which is done by a trust)

Industry/Entity Type

Real Estate

Number of Pages Required

3 page

Font styles to use
Serif
Sans Serif

Requirements
Must have
• Be in English and Spanish (I can help with translation English to Spanish); be able to update the real estate area since it changes accordingly to new listings and sales.
Nice to have
• Easy to navigate and to enter to each area of web page, we would have 3 areas the 1.- accounting and taxes
• 2.- Legal
• 3.- Real Estate

```html
<!DOCTYPE html>
<html lang="en">
<head>
<meta charset="utf-8">
<title>Cora Advisory — Real Estate, Accounting, Legal</title>
<link href="https://fonts.googleapis.com/css2?family=Oswald:wght@300;400;500&family=Roboto:wght@400;500;700&display=swap" rel="stylesheet">
<style>
:root{
  --blue:#1d5c9c;
  --orange:#f47b20;
  --ink:#2b2b2b;
  --muted:#8a8a8a;
  --line:#dcdcdc;
  --grey-bg:#f0f0f2;
  --white:#ffffff;
  --footer:#444446;
  --footer-line:#5a5a5c;
}
*{box-sizing:border-box;margin:0;padding:0}
html,body{width:1200px;height:2965px;overflow:hidden}
body{position:relative;font-family:'Roboto',sans-serif;color:var(--ink);background:var(--white)}
.abs{position:absolute}
.heading{font-family:'Oswald',sans-serif;font-weight:400}

/* header */
.site-header{position:absolute;left:0;top:0;width:1200px;height:196px;background:var(--white)}
.brand{position:absolute;left:100px;top:34px;display:flex;flex-direction:column;align-items:center}
.brand-mark{width:44px;height:44px;background:var(--orange);margin-bottom:12px}
.brand-name{font-family:'Oswald',sans-serif;font-weight:500;font-size:30px;color:var(--orange);letter-spacing:1px;line-height:1}
.brand-tag{font-size:10px;font-weight:700;color:var(--blue);letter-spacing:.6px;margin-top:6px}
.lang-select{position:absolute;left:676px;top:54px;width:134px;height:40px;border:1px solid var(--line);display:flex;align-items:center;padding:0 12px;font-size:12px;color:#555;gap:10px}
.lang-flag{width:20px;height:12px;background:linear-gradient(#b22234 0 50%,#3c3b6e 50% 100%)}
.call{position:absolute;left:854px;top:66px;display:flex;align-items:center;gap:10px;font-size:12px;font-weight:700;color:var(--ink)}
.phones{position:absolute;left:963px;top:50px;font-size:14px;font-weight:700;color:var(--ink);line-height:30px}
.phones span{font-weight:400;font-size:12px}
.main-nav{position:absolute;right:100px;top:140px;display:flex;gap:36px;font-size:12px;font-weight:500;letter-spacing:.5px;color:#555}
.main-nav .current{color:var(--ink);font-weight:700}

/* hero */
.hero{position:absolute;left:0;top:196px;width:1200px;height:664px;background:linear-gradient(120deg,#9aa0a8 0%,#c4c8cd 30%,#e6e7e9 55%,#aab6c4 80%,#1d4f8c 100%)}
.hero-title{position:absolute;left:146px;top:268px;font-size:56px;color:var(--white);line-height:1;text-shadow:0 1px 4px rgba(0,0,0,.5)}
.hero-sub{position:absolute;left:146px;top:345px;font-size:17px;font-weight:500;color:var(--white);line-height:33px;text-shadow:0 1px 4px rgba(0,0,0,.6)}
.hero-arrow{position:absolute;top:308px;width:48px;height:50px;background:var(--blue);display:flex;align-items:center;justify-content:center}
.hero-dots{position:absolute;left:545px;top:568px;display:flex;gap:8px}
.hero-dots i{width:16px;height:16px;border-radius:50%;background:var(--white);display:block}

/* search */
.search-panel{position:absolute;left:100px;top:828px;width:1000px;height:170px;background:var(--white);box-shadow:0 18px 24px -14px rgba(0,0,0,.25)}
.field{position:absolute;height:50px;border:1px solid var(--line);font-size:12px;color:#555;display:flex;align-items:center;justify-content:space-between;padding:0 14px}
.search-btn{position:absolute;left:849px;top:91px;width:134px;height:52px;background:var(--orange);color:var(--white);font-size:14px;font-weight:700;letter-spacing:.5px;display:flex;align-items:center;justify-content:center}

/* sections */
.section{position:absolute;left:0;width:1200px}
.grey{background:var(--grey-bg)}
.center-title{position:absolute;left:0;width:1200px;text-align:center;font-size:24px;color:var(--blue)}
.center-title em{font-style:normal;color:var(--orange)}
.short-rule{position:absolute;left:570px;width:60px;height:4px;background:var(--line)}
.intro{position:absolute;left:140px;width:920px;text-align:center;font-size:13.5px;line-height:27px;color:var(--muted)}
.motto{position:absolute;top:253px;font-size:17px}

.section-title{position:absolute;left:100px;font-size:24px;color:var(--blue)}
.section-rule{position:absolute;left:100px;width:1000px;height:1px;background:var(--line)}
.pager{position:absolute;left:1040px;display:flex;gap:20px;align-items:center}

.property{position:absolute;top:156px;width:230px}
.property-photo{width:230px;height:156px;position:relative}
.sale-tag{position:absolute;right:8px;top:0;width:42px;height:52px;background:var(--orange);color:var(--white);font-family:'Oswald',sans-serif;font-size:14px;line-height:17px;text-align:center;padding-top:8px}
.property-name{position:absolute;left:0;top:182px;font-family:'Oswald',sans-serif;font-weight:400;font-size:16px;color:var(--ink)}
.property-price{position:absolute;left:0;top:212px;font-family:'Oswald',sans-serif;font-weight:400;font-size:16px;color:var(--orange)}
.more-btn{position:absolute;right:2px;top:188px;width:38px;height:38px;border:1px solid var(--line);background:var(--white);display:flex;align-items:center;justify-content:center}

.subscribe-form{position:absolute;left:354px;top:189px;width:510px;height:66px;border:1px solid var(--line);background:var(--white)}
.subscribe-form .email{position:absolute;left:22px;top:0;height:64px;display:flex;align-items:center;gap:14px;font-size:13px;color:#777}
.subscribe-btn{position:absolute;right:4px;top:4px;width:148px;height:56px;background:var(--orange);color:var(--white);font-size:14px;font-weight:700;display:flex;align-items:center;justify-content:center;gap:8px;letter-spacing:.5px}

.post{position:absolute;top:144px;width:309px}
.post-photo{width:309px;height:168px}
.post-title{margin-top:30px;font-family:'Oswald',sans-serif;font-weight:400;font-size:16px;color:var(--ink)}
.post-text{margin-top:8px;font-size:13px;line-height:25px;color:var(--muted)}
.post-btn{margin-top:14px;width:28px;height:28px;background:var(--orange);display:flex;align-items:center;justify-content:center}

/* footer */
.site-footer{position:absolute;left:0;top:2661px;width:1200px;height:304px;background:var(--footer);color:var(--white)}
.foot-brand{position:absolute;left:100px;top:44px;font-family:'Oswald',sans-serif;font-size:22px}
.foot-sub{position:absolute;left:100px;top:84px;font-size:12px;font-weight:700;letter-spacing:.3px}
.foot-text{position:absolute;left:100px;top:130px;font-size:12.5px;color:#9a9a9a}
.login-title{position:absolute;left:648px;top:46px;font-family:'Oswald',sans-serif;font-size:22px}
.login-field{position:absolute;top:97px;height:48px;border:1px solid var(--footer-line);display:flex;align-items:center;gap:10px;padding:0 16px;font-size:12.5px;color:#aaa}
.login-btn{position:absolute;left:989px;top:97px;width:108px;height:48px;background:var(--orange);font-size:14px;font-weight:700;display:flex;align-items:center;justify-content:center;letter-spacing:.5px}
.foot-rule{position:absolute;left:100px;top:202px;width:1000px;height:1px;background:var(--footer-line)}
.follow{position:absolute;left:104px;top:248px;display:flex;align-items:center;gap:20px;font-size:11px;font-weight:700}
.social{width:14px;height:14px;border-radius:50%;background:var(--white);display:block}
.social.accent{background:var(--orange)}
.copyright{position:absolute;right:100px;top:250px;font-size:11px;color:#9a9a9a}
</style>
</head>
<body>

<header class="site-header">
  <div class="brand">
    <span class="brand-mark"></span>
    <span class="brand-name">CORA ADVISORY</span>
    <span class="brand-tag">REAL ESTATE, ACCOUNTING, LEGAL</span>
  </div>
  <div class="lang-select"><span class="lang-flag"></span>English
    <svg width="10" height="6" viewBox="0 0 10 6" style="margin-left:auto"><path d="M1 1l4 4 4-4" fill="none" stroke="#555" stroke-width="1.5"/></svg>
  </div>
  <div class="call">
    <svg width="16" height="16" viewBox="0 0 24 24"><path d="M6.6 10.8a15.1 15.1 0 006.6 6.6l2.2-2.2a1 1 0 011-.25 11.4 11.4 0 003.6.57 1 1 0 011 1V20a1 1 0 01-1 1A17 17 0 013 4a1 1 0 011-1h3.5a1 1 0 011 1 11.4 11.4 0 00.57 3.6 1 1 0 01-.25 1z" fill="#333"/></svg>
    CALL US
  </div>
  <div class="phones"><span>US :</span> (602) 555 0148<br><span>MX :</span> (638) 555 0172</div>
  <nav class="main-nav">
    <span class="current">HOME</span><span>ABOUT</span><span>REAL ESTATE</span><span>ACCOUNTING</span><span>LEGAL</span><span>BLOG</span><span>CONTACT</span>
  </nav>
</header>

<section class="hero" role="img" aria-label="Photo of hands working a calculator over printed tax charts">
  <h1 class="hero-title heading">Accounting Taxes</h1>
  <p class="hero-sub">We are a team of professionals advising<br>our national and international .</p>
  <div class="hero-arrow" style="left:0"><svg width="14" height="14" viewBox="0 0 14 14"><path d="M9 2L4 7l5 5" fill="none" stroke="#fff" stroke-width="2.4"/></svg></div>
  <div class="hero-arrow" style="right:0"><svg width="14" height="14" viewBox="0 0 14 14"><path d="M5 2l5 5-5 5" fill="none" stroke="#fff" stroke-width="2.4"/></svg></div>
  <div class="hero-dots"><i></i><i></i><i></i><i></i><i></i></div>
</section>

<form class="search-panel">
  <div class="field" style="left:18px;top:18px;width:212px">Property Type<svg width="10" height="6" viewBox="0 0 10 6"><path d="M1 1l4 4 4-4" fill="none" stroke="#555" stroke-width="1.5"/></svg></div>
  <div class="field" style="left:248px;top:18px;width:214px">Location<svg width="10" height="6" viewBox="0 0 10 6"><path d="M1 1l4 4 4-4" fill="none" stroke="#555" stroke-width="1.5"/></svg></div>
  <div class="field" style="left:477px;top:18px;width:210px">Select Status<svg width="10" height="6" viewBox="0 0 10 6"><path d="M1 1l4 4 4-4" fill="none" stroke="#555" stroke-width="1.5"/></svg></div>
  <div class="field" style="left:703px;top:18px;width:132px">Beds<svg width="10" height="6" viewBox="0 0 10 6"><path d="M1 1l4 4 4-4" fill="none" stroke="#555" stroke-width="1.5"/></svg></div>
  <div class="field" style="left:851px;top:18px;width:132px">Baths<svg width="10" height="6" viewBox="0 0 10 6"><path d="M1 1l4 4 4-4" fill="none" stroke="#555" stroke-width="1.5"/></svg></div>
  <div class="field" style="left:18px;top:91px;width:214px">Min Price<svg width="10" height="6" viewBox="0 0 10 6"><path d="M1 1l4 4 4-4" fill="none" stroke="#555" stroke-width="1.5"/></svg></div>
  <div class="field" style="left:250px;top:91px;width:211px">Max Price<svg width="10" height="6" viewBox="0 0 10 6"><path d="M1 1l4 4 4-4" fill="none" stroke="#555" stroke-width="1.5"/></svg></div>
  <div class="field" style="left:475px;top:91px;width:356px;height:52px">Search keyword<svg width="16" height="16" viewBox="0 0 16 16"><circle cx="6.5" cy="6.5" r="5" fill="none" stroke="#666" stroke-width="1.6"/><path d="M10.3 10.3L15 15" stroke="#666" stroke-width="1.8"/></svg></div>
  <div class="search-btn">SEARCH</div>
</form>

<section class="section" style="top:1050px;height:334px">
  <h2 class="center-title heading" style="top:42px">Welcome to <em>Cora Advisory</em></h2>
  <span class="short-rule" style="top:97px"></span>
  <p class="intro" style="top:132px">We are a team of professionals advising our national and international clients doing business in Mexico. We are a creative firm that prides itself on finding the best bespoke solutions for our clients. If the obvious doesn't work, we always look for other ways of getting a result; it's a natural aspect of how our people work putting in front our professionalism and integrity which are the soul of our company.</p>
  <p class="motto" style="left:326px;color:var(--blue)">Our people do the difference!!</p>
  <span class="abs" style="left:599px;top:252px;width:2px;height:26px;background:#bbb"></span>
  <p class="motto" style="left:635px;color:var(--ink)">Welcome, we look forward to serve you!</p>
</section>

<section class="section grey" style="top:1384px;height:445px">
  <h2 class="section-title heading" style="top:44px">Properties</h2>
  <div class="pager" style="top:42px">
    <svg width="14" height="22" viewBox="0 0 14 22"><path d="M11 2L3 11l8 9" fill="none" stroke="#bbb" stroke-width="2.6"/></svg>
    <span style="width:1px;height:22px;background:#ccc"></span>
    <svg width="14" height="22" viewBox="0 0 14 22"><path d="M3 2l8 9-8 9" fill="none" stroke="var(--orange)" stroke-width="2.6"/></svg>
  </div>
  <span class="section-rule" style="top:101px"></span>

  <article class="property" style="left:100px">
    <div class="property-photo" role="img" aria-label="Photo of a furnished living and dining room" style="background:linear-gradient(135deg,#6f5a46,#b49a7c 55%,#3f7d9a)"><span class="sale-tag">FOR<br>SALE</span></div>
    <h3 class="property-name">Casa Amarena</h3><p class="property-price">$129,000</p>
    <span class="more-btn"><svg width="8" height="12" viewBox="0 0 8 12"><path d="M1.5 1l5 5-5 5" fill="none" stroke="#999" stroke-width="1.8"/></svg></span>
  </article>
  <article class="property" style="left:356px">
    <div class="property-photo" role="img" aria-label="Aerial photo of a beach resort with pool" style="background:linear-gradient(135deg,#cdbfa6,#e2d7c2 45%,#3f8a9a 75%,#a79a84)"><span class="sale-tag">FOR<br>SALE</span></div>
    <h3 class="property-name">House In Coral Hill</h3><p class="property-price">$299,000</p>
    <span class="more-btn"><svg width="8" height="12" viewBox="0 0 8 12"><path d="M1.5 1l5 5-5 5" fill="none" stroke="#999" stroke-width="1.8"/></svg></span>
  </article>
  <article class="property" style="left:613px">
    <div class="property-photo" role="img" aria-label="Photo of a bedroom with a double bed" style="background:linear-gradient(135deg,#3d3128,#8a7a6a 50%,#c9c4c0)"><span class="sale-tag">FOR<br>SALE</span></div>
    <h3 class="property-name">House 1</h3><p class="property-price">$129,000</p>
    <span class="more-btn"><svg width="8" height="12" viewBox="0 0 8 12"><path d="M1.5 1l5 5-5 5" fill="none" stroke="#999" stroke-width="1.8"/></svg></span>
  </article>
  <article class="property" style="left:868px">
    <div class="property-photo" role="img" aria-label="Photo of a bedroom with an ocean view" style="background:linear-gradient(135deg,#4a3a28,#a07a4a 50%,#8fb3c9)"><span class="sale-tag">FOR<br>SALE</span></div>
    <h3 class="property-name">House 2</h3><p class="property-price">$129,000</p>
    <span class="more-btn"><svg width="8" height="12" viewBox="0 0 8 12"><path d="M1.5 1l5 5-5 5" fill="none" stroke="#999" stroke-width="1.8"/></svg></span>
  </article>
</section>

<section class="section" style="top:1829px;height:316px">
  <h2 class="center-title heading" style="top:46px">Subscribe To Blog Via Email</h2>
  <p class="abs" style="left:0;top:131px;width:1200px;text-align:center;font-size:13px;color:var(--muted)">Enter your email address to subscribe to this blog and receive notifications of new posts by email.</p>
  <div class="subscribe-form">
    <span class="email"><svg width="14" height="11" viewBox="0 0 14 11"><rect x="0" y="0" width="14" height="11" rx="1" fill="#888"/><path d="M0.5 1l6.5 5 6.5-5" fill="none" stroke="#fff" stroke-width="1.3"/></svg>E mail Address</span>
    <span class="subscribe-btn"><svg width="14" height="11" viewBox="0 0 14 11"><rect x="0" y="0" width="14" height="11" rx="1" fill="#fff"/><path d="M0.5 1l6.5 5 6.5-5" fill="none" stroke="var(--orange)" stroke-width="1.3"/></svg>SUBSCRIBE</span>
  </div>
</section>

<section class="section grey" style="top:2145px;height:516px">
  <h2 class="section-title heading" style="top:48px">Our Blog</h2>
  <div class="pager" style="top:46px">
    <svg width="14" height="22" viewBox="0 0 14 22"><path d="M11 2L3 11l8 9" fill="none" stroke="#bbb" stroke-width="2.6"/></svg>
    <span style="width:1px;height:22px;background:#ccc"></span>
    <svg width="14" height="22" viewBox="0 0 14 22"><path d="M3 2l8 9-8 9" fill="none" stroke="var(--orange)" stroke-width="2.6"/></svg>
  </div>
  <span class="section-rule" style="top:103px"></span>

  <article class="post" style="left:100px">
    <div class="post-photo" role="img" aria-label="Photo of a person working with a calculator at a desk" style="background:linear-gradient(135deg,#d9d9d9,#f2f2f2 50%,#6b5a4e)"></div>
    <h3 class="post-title">But I must explain to you how</h3>
    <p class="post-text">At vero eos et accusamus et iusto odio dignissi-<br>mos ducimus.</p>
    <span class="post-btn"><svg width="8" height="12" viewBox="0 0 8 12"><path d="M1.5 1l5 5-5 5" fill="none" stroke="#fff" stroke-width="2"/></svg></span>
  </article>
  <article class="post" style="left:446px">
    <div class="post-photo" role="img" aria-label="Photo of a desk with papers, glasses and a coffee cup" style="background:linear-gradient(135deg,#2e4a66,#8a6a4a 50%,#d8c9a8)"></div>
    <h3 class="post-title">On the other hand, we denounce</h3>
    <p class="post-text">which is the same as saying through shrinking<br>from toil and pain.</p>
    <span class="post-btn"><svg width="8" height="12" viewBox="0 0 8 12"><path d="M1.5 1l5 5-5 5" fill="none" stroke="#fff" stroke-width="2"/></svg></span>
  </article>
  <article class="post" style="left:789px">
    <div class="post-photo" role="img" aria-label="Photo of two businessmen on phone calls by an office window" style="background:linear-gradient(135deg,#9fb7cf,#5a6e84 50%,#2a2f38)"></div>
    <h3 class="post-title">The standard chunk of Lorem</h3>
    <p class="post-text">Malorum" by Cicero are also reproduced in their<br>exact original form, accompanied.</p>
    <span class="post-btn"><svg width="8" height="12" viewBox="0 0 8 12"><path d="M1.5 1l5 5-5 5" fill="none" stroke="#fff" stroke-width="2"/></svg></span>
  </article>
</section>

<footer class="site-footer">
  <p class="foot-brand">CORA ADVISORY</p>
  <p class="foot-sub">REAL ESTATE, LEGAL AND ACCOUNTING</p>
  <p class="foot-text">Rocky Point based company with many years of experience.</p>
  <p class="login-title">Login</p>
  <div class="login-field" style="left:650px;width:157px">
    <svg width="11" height="12" viewBox="0 0 11 12"><circle cx="5.5" cy="3" r="3" fill="#aaa"/><path d="M0 12a5.5 5 0 0111 0z" fill="#aaa"/></svg>Username</div>
  <div class="login-field" style="left:822px;width:155px">
    <svg width="10" height="12" viewBox="0 0 10 12"><rect x="0" y="5" width="10" height="7" fill="#aaa"/><path d="M2 5V3.5a3 3 0 016 0V5" fill="none" stroke="#aaa" stroke-width="1.5"/></svg>Password</div>
  <span class="login-btn">LOGIN</span>
  <span class="foot-rule"></span>
  <div class="follow">FOLLOW US ON
    <span class="social accent"></span><span class="social"></span><span class="social"></span><span class="social"></span>
  </div>
  <p class="copyright">Copyrights @ 2015 All Rights Reserved</p>
</footer>

</body>
</html>
```